Business card and stationary for a Real Estate Company.
Bartholomew Quenby
Business card and stationary for a Real Estate Company.  - Real Estate
Creative Brief
Professional
Broker
No address is to appear
bart@quenbyrealestate.example
www.QuenbyRealEstate.example
BRE 04736251
I'm looking for a business card and stationary design for a Real Estate Brokerage. Style is to be simple yet creative. Professional looking with no bold colors. Back of Card: I'd like the logo to appear on the back of the card by itself with no other text. Logo background is to be transparent. Front of Card: There should be no logo or business name just my name at the top with the word Broker immediately below my name. Then my contact information below. I'd like the information to be centered but am open to other ideas. Thank you in advance for your participation
I'd like the logo to appear on the back of the card by itself with no other text. Logo background is to be transparent.

```html
<!DOCTYPE html>
<html lang="en">
<head>
<meta charset="utf-8">
<title>Bartholomew Quenby – Business Card</title>
<link rel="stylesheet" href="https://fonts.googleapis.com/css2?family=Roboto+Condensed:wght@300;400&display=swap">
<style>
  :root{
    --backdrop:#d9d8d5;
    --card:#f4f4f3;
    --band:#3b3b3d;
    --ink:#2f2f31;
    --band-text:#f2f2f2;
  }
  html,body{margin:0;padding:0;overflow:hidden}
  body{
    width:1200px;height:940px;
    background:var(--backdrop);
    font-family:"Roboto Condensed", Arial, sans-serif;
    position:relative;
  }
  .card{
    position:absolute;left:355px;top:70px;
    width:490px;height:800px;
    background:var(--card);
    border-radius:40px;
    overflow:hidden;
    box-shadow:0 2px 6px rgba(0,0,0,.12);
  }
  .card-layout{
    position:absolute;left:-200px;top:0;
    width:900px;height:800px;
    transform:rotate(-22deg);
    transform-origin:450px 400px;
  }
  .rule{position:absolute;left:0;width:900px;height:3px;background:var(--band)}
  .rule-top{top:268px}
  .rule-bottom{top:402px}
  .band{
    position:absolute;left:0;top:282px;width:900px;height:110px;
    background:var(--band);
  }
  .person{position:absolute;left:260px;top:306px;color:var(--band-text)}
  .person-name{font-size:30px;font-weight:400;letter-spacing:1px;text-transform:uppercase;line-height:1;white-space:nowrap}
  .person-title{font-size:20px;font-weight:300;margin-top:10px}
  .contact{
    position:absolute;left:280px;top:428px;
    list-style:none;margin:0;padding:0;
    color:var(--ink);font-size:18px;font-weight:400;line-height:30px;white-space:nowrap
  }
</style>
</head>
<body>
  <div class="card">
    <div class="card-layout">
      <div class="rule rule-top"></div>
      <div class="band"></div>
      <div class="person">
        <div class="person-name">Bartholomew Quenby</div>
        <div class="person-title">Broker</div>
      </div>
      <div class="rule rule-bottom"></div>
      <ul class="contact">
        <li>055 010 24680</li>
        <li>bart@quenbyrealestate.example</li>
        <li>www.QuenbyRealEstate.example</li>
        <li>BRE 04736251</li>
      </ul>
    </div>
  </div>
</body>
</html>
```